Store Front Window Design

We have a beautiful corner store front dental practice with no window signage. Crazy I know...that's why we need your help.

The final design will be done in all vinyl unless unless you suggest a different medium (meaning we are open to some design idea like using frosted glass, etc...).

The windows provide a lot of natural light so the design needs to keep a lot of natural light coming into the office. Keep in mind vinyl is not opaque so keep the signage aesthetically pleasing and a minimalist design to allow as much natural light in as possible. The design should follow the aesthetic from our logo. or tie into at least. We want a cohesive brand aesthetic.

I submitted some general layout ideas. There is a blue banner with advertising words which we want to be used in the final version. Even though the lettering is black, in reality the letters will be a white vinyl on the outside of the window. When you submit your work, be sure to add any special instructions (aka tell me the vision for the letters is white not black, maybe gold leaf, or forested glass...stuff like that). AND YOU DO NOT HAVE TO FOLLOW MY PATTERN! YOU ARE ARTISTS AND WE ARE LOOKING FOR AN ARTISTIC EYE CATCHING PRESENTATION OF THIS INFORMATION. MAKE IT FLASHY AND ADD SOME AESTHETIC FROM THE TOOTH LOGO.

The store front is 6 windows roughly 60'' x 36'' The smaller windows below are 27'' x 36''. Around the corner there are 3 windows. they are 60'' x 27'' lower windows are 27" x 27". We would like to keep the bottom windows clear and keep the signage on the top windows, however, we are flexible.

The front 6 windows need to have this information worked into the design.

Practice name: Vesk and Ormond Dental & Orthodontics.
Phone numbers: Marisol Vesk DDS: 415.772.0183
Tobias Ormond DDS:415.509.2371

Expertise: Dr. Vesk General Dentistry & Orthodontics
Dr. Ormond Oral Surgery & Sedation

Address: 1937 Birchwood Ave

A banner across the bottom of the top windows with some key advertisement words: "Clarivet" "Braces" "Implants" "Whiting" "Call today" "Free Consultation" "Oral Surgery" "Sedation". We like the two color idea. Its up to you to decide on the color combo. I used a Dark and light blue, but maybe a Blue and grey would nice to tire in the logo colors?

I have made some mock ideas to get the ball rolling but you do not have to stick to these designs at all, just as long as all the required information is there. Be creative with the layouts, fonts, color scheme, (just remember these are going on windows not necessarily a white background), and graphics/artistic flare (refer to logo for layout inspiration and use the logo as an actual graphic). We are running a miltimillion dollar dental practice so we want these windows to be eye catching to pull in patients and look like a million dollar design. Also all 6 windows dont need ot be used. I am really looking for creative design marketing.

The corner 3 windows need the following information: name, expertise, phone number, banner.

Dr. Vesk, General Dentistry & Orthodontics, 415.772.0183
Dr. Ormond, Oral Surgery & Sedation, 415.509.2371

There is also a front door that needs to be designed. The door is 60'' x 36'' (standard door size) We want simple white vinyl on the outside of the door. We need you to organize the information on the door, pick a easy to read font, maybe use the logo and use some of the front window signage aesthetic? Its up to you...but we we were initially thinking of just making the litters white and keep it simple but again you are the designers.

Practice name: Vesk and Ormond General Dentistry & Orthodontics

Address: 1937 Birchwood Ave

Phone numbers: Dr. Vesk 415.772.0183
Dr. Ormond 415.509.2371

Hours of operation: Mon: call for an appointment
Tues-Thurs: 9am-5pm
Sat: call for an appointment
Sun: Closed

A line saying we speak Spanish: Se Habla Espanol

*****************************************************************************************************
here are some design that we liked and some rough sketches I made to start the ball rolling. Keep in mind that there are 9 windows for the front because its a corner office, but not all of them have to have stuff on it. We want simple, streamline, classy high commanding price point aesthetic. I am hiring you for your artistic minds.

Target Market(s)

anyone who has dental needs

Industry/Entity Type

Dental

Font styles to use
Serif
Sans Serif

Colors

Designer to choose colors to be used in the design.

Requirements
Must have
• 1. The required information (see project description)
• 2. Logo
• 3. Advertisement banner running along the bottom of all 9 windows (6 in front and 3 on the side)
• NOTE: Look at pictures of the store to get a sense of the customers point of view and also as a reference to how your design will be broken up across several windows or maybe you design something special for every window. But we want the banner to run along all the windows to lead customs to the door on the side. Finally the letters will be done in white vinyl unless state otherwise, remember the window needs to let in natural light so the entire window can not be covered in vinyl.
Nice to have
• artistic flare yet simple and sleep and expensive looking aesthetic. work logo into the design.
Should not have
• The goal is to catch someone eye and give them important information about the practice.
• It should not just be words.
• It should not have to many words
• It must be readable font for cards driving by.

```html
<!DOCTYPE html>
<html lang="en">
<head>
<meta charset="utf-8">
<title>Vesk and Ormond Dental &amp; Orthodontics – Window Signage</title>
<link rel="stylesheet" href="https://fonts.googleapis.com/css2?family=Lexend:wght@400;500;600&display=swap">
<style>
  :root{
    --page-bg:#d9dadc;
    --page-glow:#f4f4f5;
    --panel-light:#ececed;
    --photo-light:#f1f1f2;
    --photo-mid:#dcdcde;
    --photo-hair:#6b4a3c;
    --brand-blue:#1f73ad;
    --brand-grey:#8a8c8f;
    --ink:#2b2b2b;
    --ink-soft:#4a4a4a;
    --white:#ffffff;
    --guide:#b0324f;
  }
  *{margin:0;padding:0;box-sizing:border-box}
  html,body{width:1200px;height:1200px;overflow:hidden}
  body{
    background:radial-gradient(ellipse at 50% 55%,var(--page-glow) 0%,var(--page-bg) 85%);
    font-family:"Lexend",sans-serif;
    position:relative;
  }
  .board{
    position:absolute;
    width:1165px;height:840px;
    background:var(--white);
    box-shadow:0 3px 6px rgba(0,0,0,.35);
    overflow:hidden;
  }
  .board--main{left:22px;top:18px}
  .board--preview{
    left:392px;top:878px;
    transform:scale(.3657);
    transform-origin:0 0;
  }
  .hero-photo{
    position:absolute;left:0;top:0;width:1165px;height:692px;
    background:
      radial-gradient(ellipse 260px 340px at 880px 330px,rgba(107,74,60,.45),rgba(107,74,60,0) 70%),
      radial-gradient(ellipse 330px 260px at 870px 640px,var(--white),rgba(255,255,255,0) 75%),
      linear-gradient(90deg,var(--photo-mid),var(--photo-light) 45%,var(--photo-mid));
  }
  .info-panel{
    position:absolute;left:0;top:0;width:384px;height:692px;
    background:linear-gradient(180deg,rgba(244,244,245,.85),rgba(232,232,233,.85));
  }
  .brand{
    position:absolute;left:282px;top:70px;transform:translateX(-50%);
    text-align:center;color:var(--brand-grey);font-weight:500;white-space:nowrap;
  }
  .brand__mark{
    width:92px;height:92px;border-radius:50%;
    background:var(--brand-grey);margin:0 auto 22px;
  }
  .brand__name{font-size:21px;letter-spacing:.12em;line-height:1.25;text-transform:uppercase}
  .expertise{
    position:absolute;left:282px;top:236px;transform:translateX(-50%);
    text-align:center;white-space:nowrap;
    font-size:18.5px;font-weight:500;color:var(--ink);line-height:1.3;
  }
  .doctor{position:absolute;top:336px;width:230px;text-align:center;transform:translateX(-50%)}
  .doctor--vesk{left:96px}
  .doctor--ormond{left:288px}
  .doctor__name{color:var(--brand-blue);font-size:31px;font-weight:500;line-height:1.22;height:130px}
  .doctor__phone{color:var(--ink-soft);font-size:28px;font-weight:500;line-height:1.2;margin-top:10px}
  .address{
    position:absolute;left:222px;top:606px;
    font-size:28px;font-weight:500;color:var(--ink-soft);white-space:nowrap;
  }
  .promo-band{
    position:absolute;left:192px;top:692px;width:973px;height:148px;
    background:var(--brand-blue);color:var(--white);font-weight:500;
  }
  .promo-band__services{position:absolute;top:20px;left:0;width:100%;font-size:28.5px}
  .promo-band__services span{position:absolute;white-space:nowrap}
  .promo-band__offer{position:absolute;top:84px;left:42px;font-size:31px;white-space:nowrap}
  .fold-guides{position:absolute;left:392px;top:878px;width:426px;height:308px;pointer-events:none}
</style>
</head>
<body>

<section class="board board--main" aria-label="Window signage layout">
  <div class="hero-photo" role="img" aria-label="Photo: smiling woman with long brown hair in a white T-shirt making an OK hand sign"></div>
  <div class="info-panel"></div>
  <div class="brand">
    <div class="brand__mark"></div>
    <div class="brand__name">Vesk and Ormond<br>Dental &amp; Orthodontics</div>
  </div>
  <p class="expertise">Expertise: Dr. Vesk General Dentistry &amp; Orthodontics<br>Dr. Ormond Oral Surgery &amp; Sedation</p>
  <div class="doctor doctor--vesk">
    <p class="doctor__name">Marisol<br>Vesk DDS:</p>
    <p class="doctor__phone">415.<br>772.0183</p>
  </div>
  <div class="doctor doctor--ormond">
    <p class="doctor__name">Tobias<br>Ormond<br>DDS:</p>
    <p class="doctor__phone">415.<br>509.2371</p>
  </div>
  <p class="address">1937 Birchwood Ave</p>
  <div class="promo-band">
    <p class="promo-band__services">
      <span style="left:36px">CLARIVET</span>
      <span style="left:256px">BRACES</span>
      <span style="left:436px">IMPLANTS</span>
      <span style="left:640px">WHITING</span>
    </p>
    <p class="promo-band__offer">Call today" "Free Consultation" "Oral Surgery" "Sedation"</p>
  </div>
</section>

<section class="board board--preview" aria-hidden="true">
  <div class="hero-photo" role="img" aria-label="Photo: smiling woman with long brown hair in a white T-shirt making an OK hand sign"></div>
  <div class="info-panel"></div>
  <div class="brand">
    <div class="brand__mark"></div>
    <div class="brand__name">Vesk and Ormond<br>Dental &amp; Orthodontics</div>
  </div>
  <p class="expertise">Expertise: Dr. Vesk General Dentistry &amp; Orthodontics<br>Dr. Ormond Oral Surgery &amp; Sedation</p>
  <div class="doctor doctor--vesk">
    <p class="doctor__name">Marisol<br>Vesk DDS:</p>
    <p class="doctor__phone">415.<br>772.0183</p>
  </div>
  <div class="doctor doctor--ormond">
    <p class="doctor__name">Tobias<br>Ormond<br>DDS:</p>
    <p class="doctor__phone">415.<br>509.2371</p>
  </div>
  <p class="address">1937 Birchwood Ave</p>
  <div class="promo-band">
    <p class="promo-band__services">
      <span style="left:36px">CLARIVET</span>
      <span style="left:256px">BRACES</span>
      <span style="left:436px">IMPLANTS</span>
      <span style="left:640px">WHITING</span>
    </p>
    <p class="promo-band__offer">Call today" "Free Consultation" "Oral Surgery" "Sedation"</p>
  </div>
</section>

<svg class="fold-guides" viewBox="0 0 426 308" aria-hidden="true">
  <g stroke="var(--guide)" stroke-width="1" fill="none">
    <rect x=".5" y=".5" width="425" height="253"/>
    <line x1="70" y1="0" x2="70" y2="308"/>
    <line x1="140" y1="0" x2="140" y2="308"/>
    <line x1="214" y1="0" x2="214" y2="308"/>
    <line x1="284" y1="0" x2="284" y2="308"/>
    <line x1="354" y1="0" x2="354" y2="308"/>
  </g>
</svg>

</body>
</html>
```